Business card design needed

we are a bakery that specialises in traditional sourdough breads all shaped by hand. we are a little rustic but cater to a wide variety of people and are based in an affluent suburb. i think i would prefer lighter earthy colours. with some dark colours like bread crust maybe.

Industry/Entity Type

Bakery

Contact Information for Business Card

MAPLEFIELD BAKERY
27 KESTREL ST
SURREY HILLS
VIC 3127
PH: 03 55501942
EMAIL: maplefield@northwire.com.au

Requirements
Must have
• no photos. hand drawing would be great

```html
<!DOCTYPE html>
<html lang="en">
<head>
<meta charset="utf-8">
<title>Maplefield Bakery – Business Card</title>
<link rel="stylesheet" href="https://fonts.googleapis.com/css2?family=EB+Garamond:ital,wght@1,700&family=Della+Respira&family=Quattrocento&display=swap">
<style>
  :root {
    --stage-light: #f4f4f4;
    --stage-dark: #b3b3b3;
    --card-front: #5e3a20;
    --card-front-glow: #6e472b;
    --card-back: #53301a;
    --card-edge: #8a6440;
    --crumb: #7b4c27;
    --crumb-light: #86562e;
    --label-bg: #fbf9f6;
    --label-ink: #2a1a0e;
    --detail-ink: #eadfcf;
    --rule: #b79a7a;
  }
  * { margin: 0; padding: 0; box-sizing: border-box; }
  html, body { width: 1200px; height: 1172px; overflow: hidden; }
  body {
    position: relative;
    background: radial-gradient(ellipse at 40% 0%, var(--stage-light) 0%, #d6d6d6 55%, var(--stage-dark) 100%);
  }
  .card {
    position: absolute;
    width: 909px;
    height: 518px;
    border-radius: 10px;
    border: 1px solid var(--card-edge);
    overflow: hidden;
  }
  .card--front {
    left: 208px; top: 59px;
    background: linear-gradient(100deg, var(--card-front-glow) 0%, var(--card-front) 60%);
  }
  .card--back {
    left: 202px; top: 605px;
    background: var(--card-back);
  }
  .bread-art { position: absolute; inset: 0; width: 100%; height: 100%; }

  .owner-label {
    position: absolute;
    left: 0; top: 274px;
    width: 392px; height: 44px;
    background: var(--label-bg);
    border-radius: 0 8px 8px 0;
    font-family: "EB Garamond", serif;
    font-style: italic;
    font-weight: 700;
    font-size: 25px;
    color: var(--label-ink);
    text-align: right;
    padding-right: 18px;
    line-height: 44px;
  }
  .contact { position: absolute; left: 0; width: 909px; }
  .contact__rule {
    position: absolute; left: 0; width: 182px; height: 1px;
    background: var(--rule);
  }
  .contact__icon { position: absolute; left: 194px; width: 38px; height: 38px; }
  .contact__text {
    position: absolute; left: 239px;
    font-family: "Della Respira", serif;
    font-size: 25px;
    line-height: 34px;
    color: var(--detail-ink);
    white-space: nowrap;
  }
  .contact--phone { top: 338px; }
  .contact--email { top: 390px; }
  .contact--address { top: 443px; }

  .company-name {
    position: absolute;
    left: 40px; top: 440px;
    font-family: "Quattrocento", serif;
    font-size: 47px;
    color: #f7efe4;
    white-space: nowrap;
  }
</style>
</head>
<body>

<section class="card card--front">
  <svg class="bread-art" viewBox="0 0 909 518" role="img" aria-label="Hand-drawn illustration of a sliced sourdough loaf with dark crumb holes">
    <defs>
      <linearGradient id="crumbFront" x1="0" y1="0" x2="1" y2="1">
        <stop offset="0" stop-color="var(--crumb-light)"/>
        <stop offset="1" stop-color="var(--crumb)"/>
      </linearGradient>
    </defs>
    <polygon points="109,0 767,0 715,146 650,260 553,345 98,73" fill="url(#crumbFront)"/>
  </svg>

  <div class="owner-label">Owner Name here</div>

  <div class="contact contact--phone">
    <span class="contact__rule" style="top:17px"></span>
    <svg class="contact__icon" viewBox="0 0 24 24" aria-hidden="true">
      <path fill="#ffffff" d="M6.6 10.8a15 15 0 0 0 6.6 6.6l2.2-2.2a1 1 0 0 1 1-.25 11.4 11.4 0 0 0 3.6.6 1 1 0 0 1 1 1V20a1 1 0 0 1-1 1A17 17 0 0 1 3 4a1 1 0 0 1 1-1h3.5a1 1 0 0 1 1 1c0 1.25.2 2.45.6 3.6a1 1 0 0 1-.25 1z"/>
    </svg>
    <span class="contact__text" style="top:0">03 55501942</span>
  </div>

  <div class="contact contact--email">
    <span class="contact__rule" style="top:18px"></span>
    <svg class="contact__icon" viewBox="0 0 24 24" aria-hidden="true">
      <rect x="2" y="5" width="20" height="14" rx="1" fill="#ffffff"/>
      <path d="M2.5 5.5 12 13l9.5-7.5M2.5 18.5l7-6M21.5 18.5l-7-6" fill="none" stroke="var(--card-front)" stroke-width="1.3"/>
    </svg>
    <span class="contact__text" style="top:0">maplefield@northwire.com.au</span>
  </div>

  <div class="contact contact--address">
    <span class="contact__rule" style="top:3px"></span>
    <svg class="contact__icon" viewBox="0 0 24 24" style="top:-16px" aria-hidden="true">
      <path fill="#ffffff" d="M12 2 1 12h3v10h6v-6h4v6h6V12h3z"/>
    </svg>
    <span class="contact__text" style="top:-19px">maplefield bakery 27 kestrel st<br>ashdown park vic 3990</span>
  </div>
</section>

<section class="card card--back">
  <svg class="bread-art" viewBox="0 0 909 518" role="img" aria-label="Hand-drawn illustration of a sourdough slice with crumb holes">
    <defs>
      <linearGradient id="crumbBack" x1="0" y1="0" x2="1" y2="1">
        <stop offset="0" stop-color="var(--crumb-light)"/>
        <stop offset="1" stop-color="var(--crumb)"/>
      </linearGradient>
    </defs>
    <polygon points="26,0 863,0 774,306 628,514 0,135 0,49" fill="url(#crumbBack)"/>
  </svg>
  <div class="company-name">Company Name</div>
</section>

</body>
</html>
```